WhitePaper / Case Study Template

We are looking for a template setup in Indesign or Illustrator formatted and ready for print or digital to accomodate our writings that has a professional yet clean (modern) look. The whitepapers should not utilize images that are a blantent cliche' (i.e. closing a deal = handshaking ) please avoid this type of imagery... we are looking for creative concepts that can enhance and elevate our current brand standard.

We like whitespace and love the sutle accents of colors (ORANGE, DRK GRAY, WHITE) is the primary pallet. We are open to more creative use of more colors if done so tastfully.

We also would welcome and highly rank any creative use of vector imagery/special interest icons / diagrams to denote sections that can easiy be reused with multiple versions of this layout.

The main idea to takeaway is a template that's primarily used for whitepapers but could double for press releases by removing some of the extra assets.

I'll include one of the whitepapers/casestudies to use in the mock. we will try and follow this writing style for future cases. Additionally i've attached some other design media that we use in branding so you know what we are currently using (this is a relatively new look for us and part of our future branding effort)

Our Company is QWENTARO (QWENTAROS but HR for Human Resource ) here's a brief overview: QWENTARO is a premiere Business Transformation consulting firm providing Talent Management solutions that enable our clients’ sustained strategic success. We help clients PIV™ (Planning, Implementation, Validation) the future by partnering with them in defining their strategy, implementing solutions to address immediate business needs, and providing a clear roadmap to evolve a comprehensive talent management solution. We Execute with Excellence utilizing a proven methodology that combines project leadership and change management expertise with deep domain expertise in talent management Technology, Process, Content and Analytics. This unique QWENTARO approach results in optimal solutions that fully leverage the capabilities and strengths of our clients’ technology platforms and business processes in support of their strategic business objectives.

Reason: First time using this service and wasn't sure of the quality, or how many entries would come in. Either way I'd like to give everyone some more time and I'll provide feedback regarding some of the entries to nail down a quality print print/PDF piece. Thanks everyone!!!!

Reason: We really are pleased to see such quality designs, i'm extending the deadline one final time to give our team a few day to capture and provide some quick feedback to some of these submitted deigns... also I'm going to guarantee the project knowing we like a couple of the designs and the direction they are taking. 960556,960555,946091,947526 I'm going to post an additional update to required... to be sure the designs are Adobe Illustrator or Indesign. (indesign preferred with set styles for quick formatting.) Please indicate which format .AI or .ID the project will be delivered in as it may or may not impact the decision.

Target Market(s)

This is for HR and VP level audiences... we want to make HR look good.

Industry/Entity Type

Leadership

Requirements
Must have
• Print ready 300 DPI
CMYK
Bleed Edges
8.5" x 11"
Multiple Page Support
Should not have
• Bad Cliche' Imagery

```html
<!DOCTYPE html>
<html lang="en">
<head>
<meta charset="utf-8">
<title>QWENTARO Case Study Cover Spread</title>
<link rel="stylesheet" href="https://fonts.googleapis.com/css2?family=Questrial&display=swap">
<style>
  :root {
    --page: #ffffff;
    --backdrop: #ffffff;
    --orange: #f07a2c;
    --orange-light: #f59a5c;
    --orange-deep: #ec6e1f;
    --ink: #333333;
    --ink-soft: #555555;
    --fold: #9fb3c4;
    --edge: #d6d6d6;
    --disc-light: #f2f2f2;
    --disc-dark: #a9a9a9;
  }
  * { box-sizing: border-box; margin: 0; padding: 0; }
  html, body {
    width: 1200px; height: 848px; overflow: hidden;
    background: var(--backdrop);
    font-family: "Questrial", "Century Gothic", sans-serif;
    color: var(--ink);
  }
  .spread {
    position: absolute; left: 107px; top: 97px;
    width: 990px; height: 638px;
    background: var(--page);
    border: 1px solid var(--edge);
  }
  .feature-art {
    position: absolute; left: 136px; top: 0;
    width: 495px; height: 638px;
    background:
      radial-gradient(ellipse 60% 45% at 76% 56%, var(--orange-deep) 0%, transparent 70%),
      linear-gradient(180deg, var(--orange-light) 0%, var(--orange) 55%, var(--orange-deep) 100%);
  }
  .fold-line {
    position: absolute; left: 492px; top: 0;
    width: 1px; height: 638px;
    background: var(--fold);
  }
  .binder-disc {
    position: absolute; width: 54px; height: 54px;
    border-radius: 50%; background: var(--page);
    display: flex; align-items: center; justify-content: center;
  }
  .binder-disc::after {
    content: ""; width: 44px; height: 44px; border-radius: 50%;
    background: radial-gradient(circle at 50% 30%, var(--disc-light) 0%, var(--disc-dark) 100%);
  }
  .binder-disc--back { left: 108px; top: 183px; }
  .binder-disc--front { left: 603px; top: 183px; }
  .back-contact {
    position: absolute; right: 888px; top: 178px;
    text-align: right; font-size: 7.4px; line-height: 11px;
    color: var(--ink-soft);
  }
  .back-contact p + p { margin-top: 6px; }
  .brand {
    position: absolute; right: 56px; top: 40px;
    display: flex; align-items: center; gap: 6px;
    font-size: 19px; letter-spacing: 1px; color: var(--orange);
  }
  .brand-dot {
    width: 10px; height: 10px; border-radius: 50%;
    background: var(--orange);
  }
  .case-title {
    position: absolute; left: 668px; top: 201px;
    width: 240px;
    font-size: 14.6px; line-height: 24px; font-weight: 400;
    color: var(--ink);
  }
  .method-badge {
    position: absolute; left: 910px; top: 536px;
    width: 45px; height: 76px;
    background: var(--orange);
    display: flex; align-items: center; justify-content: center;
    color: var(--page); font-size: 12px; letter-spacing: 0.5px;
  }
</style>
</head>
<body>
  <main class="spread">
    <div class="feature-art" role="img" aria-label="Orange abstract artwork of light rays bursting from a glowing horizon over a softly streaked surface"></div>
    <div class="fold-line"></div>

    <address class="back-contact">
      <p>1-888-QWENTARO<br>www.QWENTARO.com<br>info@QWENTARO.com</p>
      <p>QWENTARO, LLC<br>4820 Larkspur Ave. N.<br>Fernvale, MN 55098</p>
      <p>© 2012 QWENTARO, LLC<br>All Rights Reserved</p>
    </address>

    <div class="binder-disc binder-disc--back"></div>
    <div class="binder-disc binder-disc--front"></div>

    <div class="brand"><span class="brand-name">QWENTARO™</span><span class="brand-dot"></span></div>

    <h1 class="case-title">Fast, Effective Upgrades of Job Descriptions Mark Maple Ridge Medical Center (MRMC) Project</h1>

    <div class="method-badge">PIV™</div>
  </main>
</body>
</html>
```